I have a small construction company that is growing. I specialize in commercial concrete and custom

I want a site that shows what we do. We specialize in custom deck design and builds. Custom home builds. Commercial concrete . project management

Target Market(s)

Commercial construction companies and custom home builders

Industry/Entity Type

Construction

Number of Pages Required

1 page

Font styles to use
Serif

Colors

Designer to choose colors to be used in the design.

Requirements
Must have
• Pictures and videos of project that we have completed or are in progress

```html
<!DOCTYPE html>
<html lang="en">
<head>
<meta charset="utf-8">
<title>Ridgeline – Commercial Construction &amp; Custom Home Builders</title>
<link href="https://fonts.googleapis.com/css2?family=Orbitron:wght@500;700&family=Open+Sans:wght@400;600;700&display=swap" rel="stylesheet">
<style>
:root{
  --orange:#f5a623;
  --orange-dark:#e08e0b;
  --ink:#2b2b2b;
  --muted:#8a8a8a;
  --light:#f1f1f1;
  --white:#ffffff;
}
*{box-sizing:border-box;margin:0;padding:0}
html,body{width:1200px;height:3774px;overflow:hidden;background:var(--white)}
body{font-family:"Open Sans",Arial,sans-serif;color:var(--ink);position:relative}
.page{position:relative;width:1200px;height:3774px;overflow:hidden}
.abs{position:absolute}

/* header */
.topbar{left:470px;top:0;width:730px;height:32px;background:var(--orange)}
.topbar .item{position:absolute;top:0;height:32px;display:flex;align-items:center;gap:8px;color:var(--white);font-weight:700}
.topbar .dot{width:20px;height:20px;border-radius:50%;background:var(--white);display:flex;align-items:center;justify-content:center}
.topbar .social{width:20px;height:20px;border-radius:50%;background:rgba(255,255,255,.55);display:inline-block}
.quote-btn{position:absolute;right:114px;top:4px;height:24px;padding:0 14px;background:#555;color:var(--white);font-size:11px;font-weight:700;display:flex;align-items:center;border-radius:2px}
.logo-box{left:112px;top:0;width:200px;height:110px;background:var(--orange);display:flex;flex-direction:column;align-items:center;justify-content:center;gap:6px}
.brand{display:flex;align-items:center;gap:8px;font-family:"Orbitron",sans-serif;font-weight:700;font-size:21px;color:var(--white)}
.brand .mark{width:14px;height:14px;background:var(--white)}
.brand-sub{font-size:8px;font-weight:700;color:var(--white);letter-spacing:.5px;text-align:center;line-height:1.3}
.nav{top:72px;left:0;width:1200px;height:24px}
.nav a{position:absolute;font-size:13px;font-weight:700;color:var(--ink);text-decoration:none;text-transform:uppercase}
.nav a.active{color:var(--orange)}

/* hero */
.hero{left:0;top:120px;width:1200px;height:560px;
  background:
    radial-gradient(ellipse 220px 260px at 860px 340px,rgba(214,232,60,.85),rgba(214,232,60,0) 70%),
    radial-gradient(ellipse 120px 110px at 860px 110px,rgba(250,196,40,.95),rgba(250,196,40,0) 75%),
    radial-gradient(ellipse 180px 200px at 600px 420px,rgba(235,228,214,.9),rgba(235,228,214,0) 70%),
    radial-gradient(ellipse 200px 260px at 420px 160px,rgba(150,160,70,.55),rgba(150,160,70,0) 70%),
    linear-gradient(100deg,#4a3b2c 0%,#7a6148 30%,#a88a66 55%,#8a6d4f 80%,#5e4a37 100%)}
.hero-band{left:0;top:202px;width:540px;height:194px;background:rgba(15,15,15,.78)}
.hero h1{left:124px;top:228px;font-family:"Orbitron",sans-serif;font-weight:700;font-size:49px;color:var(--white);line-height:1}
.hero h2{left:124px;top:290px;font-family:"Orbitron",sans-serif;font-weight:700;font-size:31px;color:var(--white)}
.btn{position:absolute;background:var(--orange);color:var(--white);font-size:12px;font-weight:700;text-transform:uppercase;padding:0 26px;height:34px;display:flex;align-items:center}
.dots{left:560px;top:536px;display:flex;gap:6px}
.dots span{width:13px;height:13px;border-radius:50%;border:2px solid var(--white)}
.dots span.on{background:var(--white)}

/* section titles */
.sec-title{left:0;width:1200px;display:flex;justify-content:center}
.sec-title .wrap{padding-bottom:10px;border-bottom:3px solid var(--orange)}
.sec-title .wrap.light{border-color:var(--white)}
.sec-title h3{font-family:"Orbitron",sans-serif;font-weight:500;font-size:29px;letter-spacing:.5px;white-space:nowrap}
.t-orange{color:var(--orange)}
.t-grey{color:#777}
.t-white{color:var(--white)}

/* welcome */
.intro{top:822px;left:0;width:1200px;text-align:center;font-size:13px;line-height:22px}
.welcome-photo{left:126px;top:885px;width:397px;height:192px;box-shadow:0 4px 10px rgba(0,0,0,.25)}
.house-photo{background:
  radial-gradient(ellipse 90px 40px at 30% 82%,rgba(240,240,240,.9),rgba(240,240,240,0) 70%),
  linear-gradient(180deg,#b9c6d2 0%,#c7d0d8 22%,#5e6166 23%,#6a6d72 40%,#d8d2c6 41%,#bfb7a8 62%,#6a5e4e 63%,#54493c 100%)}
.aim{position:absolute;left:570px;width:500px;height:100px}
.aim .icon{position:absolute;left:0;top:0;width:90px;text-align:center}
.aim .icon span{display:block;font-size:11px;font-weight:700;color:var(--orange);margin-top:4px;text-transform:uppercase}
.aim p{position:absolute;left:128px;top:6px;width:370px;font-size:11px;line-height:20px;color:var(--muted)}

/* services */
.services{left:0;top:1215px;width:1200px;height:516px;
  background:
    radial-gradient(ellipse 260px 200px at 1080px 200px,rgba(255,220,150,.5),rgba(255,220,150,0) 70%),
    radial-gradient(ellipse 300px 200px at 120px 380px,rgba(220,140,20,.45),rgba(220,140,20,0) 70%),
    linear-gradient(180deg,#f7b33d,#f4a21f)}
.card{position:absolute;top:1361px;width:226px;height:297px;background:var(--white);box-shadow:0 2px 6px rgba(0,0,0,.2)}
.card .pic{height:148px}
.card h4{margin-top:14px;text-align:center;font-size:15px;font-weight:600}
.card p{margin:10px 16px 0;text-align:center;font-size:10px;line-height:15px;color:var(--muted)}
.card .more{position:absolute;left:61px;bottom:14px;width:104px;height:26px;background:var(--orange);color:var(--white);font-size:10px;font-weight:700;display:flex;align-items:center;justify-content:center}

/* projects */
.proj{position:absolute;width:451px}
.proj-caption{left:626px;top:2146px;width:451px;height:224px;background:rgba(196,146,56,.55);display:flex;flex-direction:column;align-items:center;justify-content:center;color:var(--white)}
.proj-caption b{font-family:"Orbitron",sans-serif;font-weight:500;font-size:20px}
.proj-caption small{font-size:12px;letter-spacing:2px;margin-top:2px}

/* gallery */
.gallery{left:0;top:2491px;width:1200px;height:579px;
  background:
    radial-gradient(ellipse 260px 200px at 1080px 200px,rgba(235,238,240,.55),rgba(235,238,240,0) 70%),
    linear-gradient(180deg,#7f858b,#a9adb1 55%,#8e9296)}
.hex{position:absolute;width:182px;height:200px;clip-path:polygon(50% 0,100% 25%,100% 75%,50% 100%,0 75%,0 25%);background:var(--white)}
.hex i{position:absolute;inset:4px;clip-path:polygon(50% 0,100% 25%,100% 75%,50% 100%,0 75%,0 25%);display:block}
.hex.hover i{background:rgba(30,30,30,.82)}
.hex .cap{position:absolute;left:0;right:0;top:78px;text-align:center;color:var(--white);font-size:11px;line-height:15px;padding:0 30px}
.arrow{position:absolute;top:2780px}

/* customers */
.testi{position:absolute;top:3220px;width:456px;height:126px}
.testi .avatar{position:absolute;left:0;top:0;width:118px;height:126px;border:6px solid var(--orange)}
.testi .bubble{position:absolute;left:140px;top:12px;width:316px;height:104px;background:var(--light);padding:12px 16px}
.testi .bubble p{font-size:10px;line-height:15px;color:#666;font-style:italic}
.testi .bubble .name{margin-top:8px;font-size:14px;font-weight:700;letter-spacing:.5px}
.testi .bubble .stars{color:var(--orange);font-size:11px;margin-left:6px;letter-spacing:1px}
.testi .bubble .q{position:absolute;right:14px;bottom:4px;font-size:50px;line-height:1;color:#d6d6d6;font-family:Georgia,serif}

/* footer */
.footer{left:0;top:3409px;width:1200px;height:365px;background:linear-gradient(180deg,#262626,#1a1a1a 70%,#2a2420)}
.f-col{position:absolute;top:3452px;color:var(--white)}
.f-col h5{font-size:16px;font-weight:700;letter-spacing:.5px;text-transform:uppercase;margin-bottom:22px}
.f-links li{list-style:none;font-size:12px;line-height:28px}
.f-links li::before{content:"›";margin-right:10px}
.f-contact{display:flex;gap:10px;align-items:flex-start;font-size:12px;font-weight:600;margin-bottom:20px;line-height:17px}
.f-contact .ic{flex:0 0 22px;height:22px;border-radius:50%;background:var(--orange)}
.field{width:204px;height:30px;background:var(--white);font-size:10px;color:#888;padding:8px 10px;margin-bottom:10px}
.field.area{height:60px}
.submit{width:146px;height:28px;background:var(--orange);color:var(--white);font-size:11px;font-weight:700;display:flex;align-items:center;justify-content:center}
.f-brand{font-family:"Orbitron",sans-serif;font-weight:700;font-size:24px;color:var(--white);display:flex;align-items:center;gap:8px}
.f-brand .mark{width:16px;height:16px;background:var(--white)}
.f-social{display:flex;gap:9px;margin-top:22px;padding-left:28px}
.f-social span{width:26px;height:26px;border-radius:50%;background:var(--orange)}
.copy{position:absolute;top:3744px;font-size:10px;color:#cfcfcf;letter-spacing:.5px}
</style>
</head>
<body>
<div class="page">

  <!-- header -->
  <div class="abs topbar">
    <div class="item" style="left:14px"><span class="dot"><svg width="10" height="10" viewBox="0 0 24 24"><path d="M6.6 10.8a15 15 0 0 0 6.6 6.6l2.2-2.2c.3-.3.7-.4 1-.2 1.1.4 2.3.6 3.6.6.6 0 1 .4 1 1V20c0 .6-.4 1-1 1A17 17 0 0 1 3 4c0-.6.4-1 1-1h3.5c.6 0 1 .4 1 1 0 1.3.2 2.5.6 3.6.1.3 0 .7-.2 1z" fill="#f5a623"/></svg></span><span style="font-size:16px">555-214-0398</span></div>
    <div class="item" style="left:196px"><span class="dot"><svg width="10" height="8" viewBox="0 0 20 14"><rect x="1" y="1" width="18" height="12" fill="none" stroke="#f5a623" stroke-width="2"/><path d="M1 1l9 7 9-7" fill="none" stroke="#f5a623" stroke-width="2"/></svg></span><span style="font-size:11px;font-weight:600">hello@ridgelinebuild.com</span></div>
    <div class="item" style="left:384px;gap:5px"><span class="social"></span><span class="social"></span><span class="social"></span><span class="social"></span></div>
    <div class="quote-btn">GET A QUOTE</div>
  </div>
  <div class="abs logo-box">
    <div class="brand"><span class="mark"></span>RIDGELINE</div>
    <div class="brand-sub">COMMERCIAL CONSTRUCTION COMPANY<br>AND CUSTOM HOME BUILDERS</div>
  </div>
  <nav class="abs nav">
    <a class="active" style="left:424px">Home</a>
    <a style="left:514px">About Us</a>
    <a style="left:634px">Services</a>
    <a style="left:753px">Projects</a>
    <a style="left:873px">Gallery</a>
    <a style="left:987px">Contact Us</a>
  </nav>

  <!-- hero -->
  <section class="abs hero" role="img" aria-label="Engineer in yellow hard hat and safety vest holding plans on a building site, crew working behind">
    <div class="abs hero-band"></div>
    <h1 class="abs">Construction</h1>
    <h2 class="abs">you can count on.</h2>
    <div class="btn" style="left:124px;top:366px">Call us now</div>
    <div class="abs dots"><span></span><span class="on"></span><span></span><span></span></div>
  </section>

  <!-- welcome -->
  <div class="abs sec-title" style="top:742px"><div class="wrap">
    <h3><span class="t-orange">WELCOME TO </span><span class="t-grey">CONSTRUCTION</span></h3>
  </div></div>
  <p class="abs intro">I have a small construction company that is growing. I specialize in commercial concrete and custom. We specialize in custom deck design and builds.<br>Custom home builds. Commercial concrete . project management.</p>
  <div class="abs welcome-photo house-photo" role="img" aria-label="Newly built two-storey house with cars parked in front"></div>
  <div class="aim" style="top:912px">
    <div class="icon"><svg width="46" height="46" viewBox="0 0 46 46"><circle cx="23" cy="23" r="19" fill="none" stroke="#f5a623" stroke-width="3"/><circle cx="23" cy="23" r="11" fill="none" stroke="#f5a623" stroke-width="3"/><circle cx="23" cy="23" r="4" fill="#f5a623"/><path d="M23 23L40 6" stroke="#f5a623" stroke-width="3"/></svg><span>Our Goal</span></div>
    <p>Lorem ipsum dolor sit amet, consectetur adipiscing elit. Cursus consequat, nisl nec convallis fringilla, ipsum leo condimentum lacus, feugiat eleifend mauris ligula at tellus.</p>
  </div>
  <div class="aim" style="top:1030px">
    <div class="icon"><svg width="52" height="46" viewBox="0 0 52 46"><path d="M2 44L22 14l8 10 6-6 14 26z" fill="#f5a623"/><path d="M22 14V2h12l-3 4 3 4H22" fill="#f5a623"/></svg><span>Our Mission</span></div>
    <p>Lorem ipsum dolor sit amet, consectetur adipiscing elit. Cursus consequat, nisl nec convallis fringilla, ipsum leo condimentum lacus, feugiat eleifend mauris ligula at tellus.</p>
  </div>

  <!-- services -->
  <section class="abs services" role="img" aria-label="Faint city skyline and cranes behind an orange overlay"></section>
  <div class="abs sec-title" style="top:1280px"><div class="wrap light">
    <h3 class="t-white">CONSTRUCTION SERVICES</h3>
  </div></div>
  <article class="card" style="left:123px"><div class="pic" role="img" aria-label="Wooden deck with railings at dusk" style="background:linear-gradient(180deg,#7d8db5 0%,#a49bb0 35%,#6a5140 55%,#8a6648 75%,#4c3a2c 100%)"></div><h4>Deck Design &amp; Builds</h4><p>Lorem ipsum dolor sit amet, consec adipiscing elit. Curabitur et ex augue aliquet porta. Nullam varius mauris.</p><div class="more">READ MORE</div></article>
  <article class="card" style="left:366px"><div class="pic" role="img" aria-label="Timber frame of a custom home under construction" style="background:linear-gradient(180deg,#f1e6d2 0%,#dcbf90 40%,#c49a68 70%,#9c7648 100%)"></div><h4>Custom Home Builds</h4><p>Lorem ipsum dolor sit amet, consec adipiscing elit. Curabitur et ex augue aliquet porta. Nullam varius mauris.</p><div class="more">READ MORE</div></article>
  <article class="card" style="left:609px"><div class="pic" role="img" aria-label="Concrete parking garage interior with yellow columns" style="background:linear-gradient(180deg,#3c4657 0%,#5d6878 35%,#c9c08a 55%,#8e949a 70%,#b4b5b2 100%)"></div><h4>Commercial Concrete</h4><p>Lorem ipsum dolor sit amet, consec adipiscing elit. Curabitur et ex augue aliquet porta. Nullam varius mauris.</p><div class="more">READ MORE</div></article>
  <article class="card" style="left:852px"><div class="pic" role="img" aria-label="Site managers in hard hats reviewing a steel structure" style="background:linear-gradient(180deg,#7fa6d2 0%,#aec6de 45%,#d9a24a 70%,#c0692e 100%)"></div><h4>Project Management</h4><p>Lorem ipsum dolor sit amet, consec adipiscing elit. Curabitur et ex augue aliquet porta. Nullam varius mauris.</p><div class="more">READ MORE</div></article>

  <!-- projects -->
  <div class="abs sec-title" style="top:1792px"><div class="wrap">
    <h3><span class="t-orange">CONSTRUCTION </span><span class="t-grey">PROJECTS</span></h3>
  </div></div>
  <div class="proj house-photo" style="left:123px;top:1874px;height:227px" role="img" aria-label="Completed two-storey home with vehicles in the driveway"></div>
  <div class="proj" style="left:626px;top:1874px;height:227px;background:linear-gradient(180deg,#8fb0d4 0%,#c4d3e0 45%,#9a8e78 52%,#7b6b52 75%,#d8b84a 88%,#6e5f48 100%)" role="img" aria-label="Commercial site with excavator and trucks"></div>
  <div class="proj" style="left:123px;top:2146px;height:224px;background:linear-gradient(90deg,#b8bcc0 0%,#a7783f 25%,#8a5c2e 50%,#a7783f 75%,#b8bcc0 100%)" role="img" aria-label="Timber porch entrance of a custom home"></div>
  <div class="proj" style="left:626px;top:2146px;height:224px;background:linear-gradient(180deg,#d9c8a4,#b39a6c 55%,#8f7a52)" role="img" aria-label="Commercial concrete slab site"></div>
  <div class="abs proj-caption"><b>COMMERCIAL CONCRETE</b><small>(HARBOR CITY U.S.A)</small></div>
  <div class="btn" style="left:546px;top:2392px;height:30px;font-size:11px">View more</div>

  <!-- gallery -->
  <section class="abs gallery" role="img" aria-label="Faded photo of a large suburban home"></section>
  <div class="abs sec-title" style="top:2547px"><div class="wrap light">
    <h3 class="t-white">CONSTRUCTION GALLERY</h3>
  </div></div>
  <div class="hex" style="left:216px;top:2636px" role="img" aria-label="Blue-sided family home"><i style="background:linear-gradient(180deg,#7fa8d8,#8aa0b8 45%,#55728f 60%,#5c8a3a)"></i></div>
  <div class="hex" style="left:412px;top:2636px" role="img" aria-label="Modern kitchen interior"><i style="background:linear-gradient(180deg,#4a3e34,#9b8470 50%,#3e342c)"></i></div>
  <div class="hex" style="left:606px;top:2636px" role="img" aria-label="Office interior with glass walls"><i style="background:linear-gradient(180deg,#2f4a78,#c7d2e0 55%,#7d8ea4)"></i></div>
  <div class="hex" style="left:802px;top:2636px" role="img" aria-label="Craftsman house with stone porch"><i style="background:linear-gradient(180deg,#5e7089,#6a5c4e 55%,#6f8a45)"></i></div>
  <div class="hex" style="left:120px;top:2800px" role="img" aria-label="Empty warehouse interior"><i style="background:linear-gradient(180deg,#c9c2b5,#e6e2da 55%,#a79e90)"></i></div>
  <div class="hex" style="left:314px;top:2800px" role="img" aria-label="Polished concrete floor in hall"><i style="background:linear-gradient(180deg,#5f6a74,#b8c0c4 55%,#dfe3e5)"></i></div>
  <div class="hex hover" style="left:508px;top:2800px" role="img" aria-label="Gallery photo with caption overlay"><i></i><div class="cap">Lorem ipsum dolor sit amet, consectetur<br><svg width="18" height="18" viewBox="0 0 20 20" style="margin-top:8px"><circle cx="8" cy="8" r="6" fill="none" stroke="#fff" stroke-width="2"/><path d="M12.5 12.5L18 18" stroke="#fff" stroke-width="2.5"/></svg></div></div>
  <div class="hex" style="left:707px;top:2800px" role="img" aria-label="Modern white house with lawn"><i style="background:linear-gradient(180deg,#9ab8d8,#e4e4e0 55%,#6d8d4a)"></i></div>
  <div class="hex" style="left:900px;top:2800px" role="img" aria-label="Industrial hall with bright floor"><i style="background:linear-gradient(180deg,#3e5f8c,#9fb6cf 55%,#e8eef2)"></i></div>
  <svg class="arrow" style="left:60px" width="22" height="44" viewBox="0 0 22 44"><path d="M20 2L3 22l17 20" fill="none" stroke="#fff" stroke-width="2"/></svg>
  <svg class="arrow" style="left:1118px" width="22" height="44" viewBox="0 0 22 44"><path d="M2 2l17 20L2 42" fill="none" stroke="#fff" stroke-width="2"/></svg>
  <div class="abs" style="left:595px;top:2990px;width:9px;height:9px;border-radius:50%;background:#fff"></div>

  <!-- customers -->
  <div class="abs sec-title" style="top:3134px"><div class="wrap">
    <h3><span class="t-orange">CONSTRUCTION </span><span class="t-grey">CUSTOMERS</span></h3>
  </div></div>
  <div class="testi" style="left:123px">
    <div class="avatar" role="img" aria-label="Portrait of a male client" style="background:linear-gradient(180deg,#d4d7dc,#9aa3ad 60%,#3d4656)"></div>
    <div class="bubble"><p>"Donec mattis consequat pharetra. Pellentesque egestas turpis eget mauris elementum mollis. Vel nisi integer viverra. Ut cum evenit facilisim."</p><div class="name">MARCUS HALE<span class="stars">★★★★★</span></div><span class="q">”</span></div>
  </div>
  <div class="testi" style="left:621px">
    <div class="avatar" role="img" aria-label="Portrait of a female client" style="background:linear-gradient(180deg,#e4dcd2,#d8c29a 50%,#c9b8a6)"></div>
    <div class="bubble"><p>"Donec mattis consequat pharetra. Pellentesque egestas turpis eget mauris elementum mollis. Vel nisi integer viverra. Ut cum evenit facilisim."</p><div class="name">LENA ORTIZ<span class="stars">★★★★★</span></div><span class="q">”</span></div>
  </div>

  <!-- footer -->
  <footer class="abs footer" role="img" aria-label="Dark wood texture background"></footer>
  <div class="f-col" style="left:123px"><h5>Quick Links</h5>
    <ul class="f-links"><li>Home</li><li>About Us</li><li>Services</li><li>Projects</li><li>Gallery</li><li>Contact Us</li></ul>
  </div>
  <div class="f-col" style="left:332px;width:230px"><h5>Contact Info</h5>
    <div class="f-contact"><span class="ic"></span><span>Commercial construction<br>company, Harbor City,<br>U.S.A 40217</span></div>
    <div class="f-contact"><span class="ic"></span><span>555-214-0398</span></div>
    <div class="f-contact"><span class="ic"></span><span>hello@ridgelinebuild.com</span></div>
  </div>
  <div class="f-col" style="left:591px"><h5>Quick Contact</h5>
    <div class="field">Name</div><div class="field">Email</div><div class="field area">Message</div>
    <div class="submit">SUBMIT INFO</div>
  </div>
  <div class="f-col" style="left:873px"><h5>Follow Us</h5>
    <div class="f-brand" style="margin-top:40px"><span class="mark"></span>RIDGELINE</div>
    <div class="brand-sub" style="margin-top:6px">COMMERCIAL CONSTRUCTION COMPANY<br>AND CUSTOM HOME BUILDERS</div>
    <div class="f-social"><span></span><span></span><span></span><span></span></div>
  </div>
  <div class="copy" style="left:123px">© COPYRIGHT 2016 CONSTRUCTION. ALL RIGHTS RESERVED.</div>
  <div class="copy" style="left:988px">PRIVACY POLICY</div>

</div>
</body>
</html>
```